We are looking for a new website design for our SEO WEB Development Company. The URL is www.brellowcreativeworks.com

We want it to be a more powerful representation of what we do. We are also looking for a number of designers that we will give continuous business to every month. The persons design we choose will also get a proposal to complete 4 - 6 new designs for us every month for our clients.

Be creative as you can in your design submissions. We really want to stand out!

Just to give you an idea of what we like look at this site: http://www.tovandigitalstudio.com/

```html
<!DOCTYPE html>
<html lang="en">
<head>
<meta charset="utf-8">
<title>Brellow Interactive Group</title>
<link rel="stylesheet" href="https://fonts.googleapis.com/css2?family=Arimo:wght@400;700&family=Oswald:wght@500;600&family=Roboto+Condensed:wght@400&display=swap">
<style>
:root{
  --orange:#e07a1c;
  --orange-light:#f4a04a;
  --orange-dark:#c9651a;
  --red:#e0262e;
  --green:#5a9e2a;
  --green-light:#8cc63f;
  --ink:#222;
  --text:#333;
  --muted:#666;
  --rule:#d4d4d4;
  --page:#eeeeee;
  --footer:#7d7d7d;
  --yellow:#ffcc1a;
}
*{box-sizing:border-box;margin:0;padding:0}
html,body{width:667px;height:1200px;overflow:hidden}
body{position:relative;background:var(--page);font-family:"Arimo",Arial,sans-serif;color:var(--text)}
.abs{position:absolute}

.header{left:0;top:0;width:667px;height:79px;background:linear-gradient(#fff,#fdf1e6)}
.brand{left:15px;top:14px;width:120px}
.brand-name{font-size:28px;font-weight:700;color:var(--orange-dark);line-height:1}
.brand-sub{font-size:9px;color:#555;letter-spacing:.5px;margin-top:3px}
.quote-label{right:22px;top:17px;font-size:10.5px;font-weight:700;color:#111}
.phone{left:499px;top:32px;width:149px;height:38px;border-radius:10px;background:linear-gradient(#ffe066,#ffc400 55%,#f0a800);border:2px solid #f0b000;box-shadow:0 2px 3px rgba(0,0,0,.25);font-size:18px;font-weight:700;color:#111;display:flex;align-items:center;justify-content:center}

.nav{left:0;top:79px;width:667px;height:37px;background:linear-gradient(var(--orange-light),var(--orange) 60%,var(--orange-dark));display:flex}
.nav a{color:#fff;text-decoration:none;font-size:12px;font-weight:700;display:flex;align-items:center;justify-content:center;border-right:1px solid #f7b779;height:100%}
.nav .active{background:linear-gradient(#f2636b,var(--red))}

.panel{left:14px;top:128px;width:639px;height:952px;background:#fff;box-shadow:0 0 4px rgba(0,0,0,.2)}
.hero{left:22px;top:136px;width:624px;height:233px;background:linear-gradient(100deg,#9cc9a0 0%,#6fa46d 35%,#8fbf6a 60%,#d9eecd 100%)}
.hero-title{left:289px;top:171px;width:358px;height:41px;background:#000;color:#fff;font-family:"Roboto Condensed",sans-serif;font-size:31px;display:flex;align-items:center;justify-content:center}
.hero-line1{left:311px;top:220px;font-family:"Roboto Condensed",sans-serif;font-size:33px;color:#111}
.hero-line2{left:311px;top:260px;font-family:"Roboto Condensed",sans-serif;font-size:20px;color:#111}
.hero-tag{left:312px;top:294px;width:310px;height:22px;background:#000;color:#fff;font-family:"Roboto Condensed",sans-serif;font-size:16px;display:flex;align-items:center;justify-content:center;letter-spacing:.5px}

.section-bar{left:22px;top:369px;width:624px;height:28px;background:var(--orange);color:#fff;font-family:"Oswald",sans-serif;font-weight:600;font-size:24px;line-height:28px;padding-left:10px}

.service{top:416px;width:121px;height:224px}
.service-icon{position:absolute;left:3px;top:0;width:26px;height:34px;border-radius:4px}
.service-head{position:absolute;left:32px;top:6px;font-size:13px;color:#111;line-height:1}
.service-head small{display:block;font-size:8.5px;color:#555;margin-top:1px}
.service p{position:absolute;left:4px;top:50px;width:116px;font-size:7px;line-height:12px;color:#222}
.more{position:absolute;left:4px;top:191px;width:46px;height:12px;background:#3f3f3f;color:#fff;font-size:6.5px;display:flex;align-items:center;justify-content:center;border-radius:1px}
.vrule{top:416px;width:0;height:224px;border-left:1px dashed var(--rule)}

.hrule{left:22px;top:657px;width:624px;border-top:1px dashed var(--rule)}
.about{left:19px;top:674px;width:359px}
.about p{font-size:7.9px;line-height:13.6px;color:#222;margin-bottom:13.6px}
.tag{background:var(--orange);color:#fff;padding:0 1px}
.col-rule{left:397px;top:674px;height:390px;border-left:1px dashed var(--rule)}

.rep-title{left:407px;top:678px;color:var(--green);font-size:15px;line-height:17px;width:180px}
.rep-title span{display:block;padding-left:3px;font-size:12.5px}
.rep-icon{left:596px;top:668px;width:52px;height:44px}
.rep-text{left:410px;top:719px;width:228px;font-size:7.9px;line-height:13.6px;color:#222}
.form-label{font-size:7.9px;color:#222;text-align:right;width:73px;left:410px}
.field{left:490px;width:152px;height:17px;border-radius:7px;background:#efefef;border:1px solid #ddd}
.submit{left:595px;top:1015px;width:47px;height:17px;border-radius:7px;background:linear-gradient(#8cd152,#4f9b26);color:#fff;font-size:8.5px;font-weight:700;display:flex;align-items:center;justify-content:center}

.engines{left:0;top:1087px;width:667px;height:43px;background:#fff;border-top:3px solid #ddd;border-bottom:3px solid #ddd}
.engines-label{left:18px;top:1097px;font-size:14px;color:#555}
.engine{top:1098px;font-size:15px;font-weight:700;color:#555}

.footer{left:0;top:1135px;width:667px;height:65px;background:linear-gradient(#8a8a8a,var(--footer))}
.copyright{left:15px;top:1147px;font-size:8px;color:#fff}
.footer-nav{right:12px;top:1147px;font-size:8px;color:#fff;word-spacing:1px}
</style>
</head>
<body>

<header class="abs header"></header>
<div class="abs brand">
  <div class="brand-name">Brellow</div>
  <div class="brand-sub">INTERACTIVE GROUP</div>
</div>
<div class="abs quote-label">Call us for a quote today:</div>
<div class="abs phone">214-555-0147</div>

<nav class="abs nav">
  <a class="active" style="width:67px">Home</a>
  <a style="width:105px">Creative Design</a>
  <a style="width:103px">Website Design</a>
  <a style="width:167px">Internet Marketing Services</a>
  <a style="width:95px">IT Consulting</a>
  <a style="width:130px;border-right:0">Brellow Interactive</a>
</nav>

<div class="abs panel"></div>
<div class="abs hero" role="img" aria-label="Business people shaking hands in silhouette before a green glow with a hand-drawn strategy sketch"></div>
<div class="abs hero-title">Media Marketing Experts</div>
<div class="abs hero-line1">Focusing on your brand</div>
<div class="abs hero-line2">With the right Internet Marketing tools</div>
<div class="abs hero-tag">Not &nbsp;only &nbsp;Brellow &nbsp;But &nbsp;Solutions</div>

<div class="abs section-bar">What we do</div>

<div class="abs service" style="left:22px">
  <div class="service-icon" role="img" aria-label="Creative design icon" style="background:#e8891c"></div>
  <div class="service-head">CREATIVE<small>design</small></div>
  <p>Separate yourself from the crowd with smart thinking, sound strategy and solid concepts. Whether you are just starting and want to "invent" yourself for the first time, or you're an established business looking to "re-invent," now is the time. At Brellow Interactive Group, we have the experience and expertise to deliver on-time and on-budget.</p>
  <div class="more">read more..</div>
</div>
<div class="abs vrule" style="left:147px"></div>
<div class="abs service" style="left:154px">
  <div class="service-icon" role="img" aria-label="Internet marketing globe icon" style="background:#6aa7d8"></div>
  <div class="service-head">INTERNET<small>marketing services</small></div>
  <p>Brellow Interactive Group offers complete web marketing packages that put your business in the right place at the right time for the right customers–all at the right price!</p>
  <div class="more">read more..</div>
</div>
<div class="abs vrule" style="left:272px"></div>
<div class="abs service" style="left:279px">
  <div class="service-icon" role="img" aria-label="Website design tools icon" style="background:#3d7cc9"></div>
  <div class="service-head">WEBSITE<small>design</small></div>
  <p>Let Brellow Interactive Group of Dallas assist with your Web design and development through our services, which include Web application, E-commerce with on-line shopping systems, multimedia and Search Engine Optimization.</p>
  <div class="more">read more..</div>
</div>
<div class="abs vrule" style="left:397px"></div>
<div class="abs service" style="left:404px">
  <div class="service-icon" role="img" aria-label="IT consulting question mark icon" style="background:#2f7fc0;width:20px"></div>
  <div class="service-head" style="left:26px;top:9px">IT Consulting</div>
  <p>Brellow Interactive Group provides superior technology project management and integra-tion consulting services to companies from the Top 500 to IT startups. We work as technology project delivery executives in partnership with business leaders to chart a course, maintain direction, navigate challenges…</p>
  <div class="more">read more..</div>
</div>
<div class="abs vrule" style="left:522px"></div>
<div class="abs service" style="left:529px">
  <div class="service-icon" role="img" aria-label="Interactive speech bubbles icon" style="background:#7cbf3a"></div>
  <div class="service-head">BRELLOW<small>interactive</small></div>
  <p>* &nbsp;An exclusive focus on tech-nology program and project management and integration services<br><br>* The experience to create order out of chaos<br><br>* An outstanding track record--even with the toughest projects</p>
  <div class="more">read more..</div>
</div>

<div class="abs hrule"></div>

<div class="abs about">
  <p><span class="tag">Brellow Interactive Group</span> is a leading Dallas Web Site Design, Publishing and Internet Marketing Firm. Our Dallas Texas based Website Design and Internet Marketing experts are some of the best in the industry!</p>
  <p><span class="tag">Brellow Interactive Web</span> is a full-service Dallas based Advertising Agency comprised of experi-enced advertising and marketing professionals that provide clients with a clear and distinct voice in the marketplace. Web Site Design and Internet Marketing experts at our Dallas location spe-cialize in developing Online Marketing Strategies, Search Engine Marketing and Optimization (SEO), Pay Per Click , Web Site Design and Development, and Online Reputation Management.</p>
  <p><span class="tag">Brellow Interactive Publishing</span> provides full-service custom publishing and consulting services for magazines, newsletters, blogs and web sites. We are the complete interactive publishing arm for your organization. Our services include: Strategic Planning and Computer Modeling; Art Direction and Design; Production Services; Circulation Marketing and Management; Subscription Fulfillment Management; Advertising Sales Management; Web Site and Digital Magazine Design and Management; and Video Streaming Services.</p>
  <p><span class="tag">Brellow Interactive Media</span> provides cost-effective Web Site Design services, Search Engine Marketing, Internet Advertising, Internet Marketing Campaigns and most important, we can accommodate any budget.</p>
  <p><span class="tag">Brellow Interactive Reputation Management and Repair</span> provides reputation management and repair services to the online community. We offer a plan of action to create a process of tracking an entity's actions and other entities' opinions about those actions; reporting on those actions and opinions; and reacting to that report creating a feedback loop. Reputation management has become essential with the advent of widespread computing. Reputation management systems use predefined criteria for processing complex data to report the many factors affecting a company's reputation. However, these systems only facilitate and automate the process of deter-mining trustworthiness.</p>
</div>
<div class="abs col-rule"></div>

<div class="abs rep-title">Get A Free Reputation<span>Management &amp; Repair Quote!</span></div>
<svg class="abs rep-icon" viewBox="0 0 62 58" preserveAspectRatio="none" role="img" aria-label="Green speech bubble with quotation marks">
  <path d="M6 4h50a4 4 0 0 1 4 4v30a4 4 0 0 1-4 4H26l-12 14 2-14H6a4 4 0 0 1-4-4V8a4 4 0 0 1 4-4z" fill="#fff" stroke="#5a9e2a" stroke-width="3"/>
  <rect x="16" y="14" width="10" height="10" fill="#5a9e2a"/><rect x="34" y="14" width="10" height="10" fill="#5a9e2a"/>
</svg>
<div class="abs rep-text">The goal of a reputation management or repair campaign is to create and/or strengthen an authoritative, positive image of your company by helping you gain positive name recognition across a wide range of websites. Most Search Engine users only pay attention to the Top 20 results, which is what we focus on. We will work closely with you to come up with a strong, detailed plan to put you at the top of search engins such as Searchly.com and above the negative listings about you. We will analyze your situation closely and create a detailed but flexible plan for your Reputation Management Campaign.</div>

<div class="abs form-label" style="top:894px">Enter Your Name:</div>
<div class="abs field" style="top:891px"></div>
<div class="abs form-label" style="top:915px">Enter Email Id:</div>
<div class="abs field" style="top:912px"></div>
<div class="abs form-label" style="top:936px">Enter Phone No.:</div>
<div class="abs field" style="top:933px"></div>
<div class="abs form-label" style="top:956px">Enter Your Query :</div>
<div class="abs field" style="top:955px;height:51px"></div>
<div class="abs submit">Submit</div>

<div class="abs engines"></div>
<div class="abs engines-label">Here's where we do it</div>
<div class="abs engine" style="left:190px">Searchly</div>
<div class="abs engine" style="left:274px">Vistaquest</div>
<div class="abs engine" style="left:357px">Yodelo</div>
<div class="abs engine" style="left:427px">Netmo</div>
<div class="abs engine" style="left:490px">Overlane</div>
<div class="abs engine" style="left:574px">Webwide</div>

<footer class="abs footer"></footer>
<div class="abs copyright">Copyright 2011. All rights reserved.</div>
<div class="abs footer-nav">Home &nbsp;| &nbsp;Creative Design &nbsp;| &nbsp;Website Design &nbsp;| &nbsp;Internet Marketing Services &nbsp;| &nbsp;IT Consulting &nbsp;| &nbsp;Brellow Interactive</div>

</body>
</html>
```